Frozen Yoghurt Flyer Design Project

Hello, we are looking for a flyer design for a frozen yoghurt shop competition called 'Top Zelmi' (Zelmi is the shop name). This competition rule is simply post your yoghurt creation on Zelmi Chatterly and tag #topzelmi, who's frozen yoghurt gets the most vote win the game(for more details tell people please check Zelmi Chatterly). The total prize is up to $2,500, and they will also get a chance to win an tabvue2 with custom Zelmi vinyl cover.
We would like to see designs that use the colors black, white and pink. The final design should focus on attract school students, teenagers, college girls, and encourage them to come join the game with their friends.
school students, teenagers, college girls
competition starts on 19th July 2013, and ends 30th Oct. 2013
@ZELMI FROZEN YOGHURT MARLOW ARCADE EAST ( next to Brantly's)
College

```html
<!DOCTYPE html>
<html lang="en">
<head>
<meta charset="utf-8">
<title>Top Zelmi Competition Flyer</title>
<link rel="stylesheet" href="https://fonts.googleapis.com/css2?family=Bebas+Neue&family=Anton&family=Great+Vibes&family=Montserrat:wght@400&display=swap">
<style>
  :root {
    --pink-deep: #8c1482;
    --pink: #c21fa8;
    --pink-bright: #e23cc4;
    --black: #0b0b10;
    --panel-dark: #14141c;
    --white: #ffffff;
    --lilac: #d9b8f0;
    --lilac-deep: #a37ed8;
    --silver-light: #ffffff;
    --silver-mid: #bdbdc6;
    --silver-dark: #5d5d66;
  }
  * { margin: 0; padding: 0; box-sizing: border-box; }
  html, body { width: 832px; height: 1200px; overflow: hidden; background: var(--black); }
  .flyer {
    position: relative;
    width: 832px;
    height: 1200px;
    overflow: hidden;
    background:
      repeating-linear-gradient(135deg, rgba(255,255,255,0.04) 0 2px, transparent 2px 6px),
      linear-gradient(160deg, var(--pink-bright) 0%, var(--pink) 45%, var(--pink-deep) 100%);
    font-family: "Bebas Neue", "Anton", sans-serif;
  }
  .top-band {
    position: absolute; left: 0; top: 0; width: 832px; height: 150px;
    background: repeating-linear-gradient(135deg, #1c1c24 0 2px, #101016 2px 6px);
    display: flex; align-items: center; justify-content: center;
  }
  .prize-headline {
    font-family: "Anton", "Bebas Neue", sans-serif; font-weight: 400;
    font-size: 66px; letter-spacing: 2px; line-height: 1.3;
    background: linear-gradient(180deg, var(--white) 0%, var(--lilac) 50%, var(--lilac-deep) 100%);
    -webkit-background-clip: text; background-clip: text; color: transparent;
  }
  .logo-panel {
    position: absolute; left: 40px; top: 164px; width: 762px; height: 571px;
    background:
      radial-gradient(ellipse at 60% 88%, rgba(255,230,200,0.55) 0%, rgba(255,160,220,0.18) 18%, transparent 40%),
      linear-gradient(175deg, transparent 8%, rgba(120,170,255,0.35) 14%, transparent 22%),
      radial-gradient(ellipse at 50% 40%, #2a2a36 0%, var(--panel-dark) 70%);
  }
  .logo-panel .light-streaks { position: absolute; inset: 0; }
  .brand {
    position: absolute; left: 0; right: 0; top: 170px;
    text-align: center; color: var(--white);
    font-family: "Montserrat", sans-serif; font-weight: 400;
  }
  .brand-name { font-size: 150px; letter-spacing: 24px; line-height: 1; }
  .brand-tagline { margin-top: 90px; font-size: 40px; letter-spacing: 6px; }
  .black-wedge { position: absolute; left: 0; top: 0; width: 832px; height: 1200px; }
  .competition-title {
    position: absolute; left: 270px; width: 520px; top: 745px;
    padding: 20px 10px 10px;
    text-align: center; font-weight: 400;
    font-family: "Great Vibes", cursive; font-size: 106px; line-height: 1.1;
    background: linear-gradient(180deg, var(--silver-light) 25%, var(--silver-mid) 55%, var(--silver-dark) 80%, var(--silver-light) 100%);
    -webkit-background-clip: text; background-clip: text; color: transparent;
  }
  .competition-name {
    position: absolute; left: 270px; width: 520px; top: 848px;
    text-align: center; font-weight: 400;
    font-family: "Anton", sans-serif; font-size: 100px; line-height: 1.1; letter-spacing: 1px;
    background: linear-gradient(180deg, var(--silver-light) 10%, var(--silver-mid) 50%, var(--silver-dark) 75%, var(--silver-light) 100%);
    -webkit-background-clip: text; background-clip: text; color: transparent;
  }
  .call-to-action {
    position: absolute; left: 62px; top: 970px;
    font-size: 53px; line-height: 1; color: var(--white); letter-spacing: 1px;
    text-shadow: 0 0 3px var(--black), 2px 2px 0 var(--black), -1px -1px 0 var(--black);
  }
  .rules {
    position: absolute; left: 40px; width: 832px; top: 1040px;
    text-align: center; color: var(--white);
    font-size: 34px; line-height: 44px; letter-spacing: 0.5px;
  }
</style>
</head>
<body>
<main class="flyer">
  <header class="top-band">
    <h1 class="prize-headline">WIN AN TABVUE, WIN $2500</h1>
  </header>

  <section class="logo-panel">
    <div class="light-streaks" role="img" aria-label="Glowing blue and pink light streaks over a dark background"></div>
    <div class="brand">
      <div class="brand-name">ZELMI</div>
      <div class="brand-tagline">FROZEN YOGHURT</div>
    </div>
  </section>

  <svg class="black-wedge" viewBox="0 0 832 1200" aria-hidden="true">
    <polygon points="0,958 832,756 832,888 0,1012" fill="#0b0b10"/>
  </svg>

  <h2 class="competition-title">Competition</h2>
  <h2 class="competition-name">Top Zelmi</h2>

  <p class="call-to-action">SIMPLY POST YOUR YOGHURT CREATION ON</p>
  <p class="rules">
    ZELMI CHATTERLY AND TAG #TOPZELMI. WHO’S FROZEN YOGHURT<br>
    GETS THE MOST VOTE WIN THE GAME<br>
    FOR MORE DETAILS PLEASE CHECK ZELMI
  </p>
</main>
</body>
</html>
```